Political Mail Out Quintero front and back

Front
Esteban (9th Grade) Quintero!

What's that famous saying?

Show me who your friends are and I'll tell you who you really are!
(show the two guys)

Arturo Benavides is charged with voter fraud by changing voter addresses from across the RGV so they could vote in Edinburg
Back
Did Esteban (9th Grade) Quintero commit voter fraud when he ran for office in 2016?
(insert blurred photo)

Here is a list of people from all over the RGV that voted in Edinburg in the 2016 race.
Here is a break down:

(highlight the number and where they were first registered to vote)

9 People voted in Edinburg who were registered in Donna.
13 People voted in Edinburg who were registered in San Juan
8 People voted in Edinburg who were registered in Pharr
31 People voted in Edinburg who were registered in McAllen
2 People voted in Edinburg who were registered in La Joya
6 People voted in Edinburg who were registered in Edcouch
2 People voted in Edinburg who were registered in Mercedes
2 People voted in Edinburg who were registered in Monte Alto
6 People voted in Edinburg who were registered in Weslaco
1 Person voted in Edinburg who were registered in Penitas
3 People voted in Edinburg who were registered in Alamo
5 People voted in Edinburg who were registered in Elsa
6 People voted in Edinburg who were registered in Mission
1 Person voted in Edinburg who were registered in Alton

Will Esteban (9th Grade) Quintero CHEAT in 2020?

Only time will tell.

Vote Esteban (9th Grade) Quintero OUT of office.

```html
<!DOCTYPE html>
<html lang="en">
<head>
<meta charset="utf-8">
<title>Quintero Mail Out – Front and Back</title>
<link rel="stylesheet" href="https://fonts.googleapis.com/css2?family=Bebas+Neue&family=Rubik:wght@400;700&display=swap">
<style>
:root{
  --stage:#3b3b3d;
  --sky:#a6daf3;
  --sky-light:#cbeafa;
  --red:#d8222a;
  --ink:#2f2f31;
  --panel:#3a3a3c;
  --white:#ffffff;
  --cream:#fff4e2;
}
*{box-sizing:border-box;margin:0;padding:0}
html,body{width:1200px;height:806px;overflow:hidden;background:var(--stage)}
.canvas{position:relative;width:1200px;height:806px}
.card{position:absolute;top:62px;width:527px;height:682px;overflow:hidden;
  background:radial-gradient(circle at 50% 45%,var(--sky-light),var(--sky) 70%);
  box-shadow:0 4px 12px rgba(0,0,0,.45)}
.card--front{left:62px}
.card--back{left:610px}
.heading{font-family:"Bebas Neue",sans-serif;line-height:1;letter-spacing:.01em;white-space:nowrap}

/* front */
.title{position:absolute;top:48px;left:0;width:100%;display:flex;justify-content:center;align-items:center;gap:10px;color:var(--red);font-weight:400}
.title__name{font-size:74px}
.title__grade{font-size:30px;color:var(--ink);line-height:.86;text-align:center}
.front__band{position:absolute;top:134px;left:0;width:100%;height:436px;background:var(--red)}
.quote-frame{position:absolute;left:24px;top:44px;width:480px;height:322px;border:4px solid var(--white);border-top:none}
.quote-frame__top{position:absolute;top:0;height:4px;background:var(--white);width:82px}
.quote-frame__top--l{left:0}.quote-frame__top--r{right:0}
.quote-ask{position:absolute;top:35px;left:0;width:100%;text-align:center;color:var(--cream);font-size:24px}
.quote{position:absolute;top:68px;left:0;width:100%;text-align:center;color:var(--cream);font-size:35px;line-height:37px}
.friends-photo{position:absolute;left:54px;top:153px;width:418px;height:253px;border:4px solid var(--white);
  background:linear-gradient(120deg,#6b5744 0%,#b58a6a 35%,#e9e3da 55%,#6f7272 80%,#4c4f52 100%)}
.front__note{position:absolute;top:591px;left:0;width:100%;text-align:center;color:var(--ink);font-size:21px;line-height:26px}

/* back */
.question-panel{position:absolute;top:28px;left:25px;width:478px;height:208px;background:var(--panel)}
.question{position:absolute;left:32px;top:52px;color:var(--white);font-size:23px;line-height:29.6px;font-weight:400}
.roster-photo{position:absolute;left:252px;top:4px;width:222px;height:204px;
  background:linear-gradient(90deg,#9c9c9c 0%,#d8d8d8 18%,#eaeaea 60%,#cfcfcf 100%)}
.back__band{position:absolute;top:236px;left:0;width:100%;height:334px;background:var(--red)}
.list-intro{position:absolute;top:16px;left:0;width:100%;text-align:center;color:var(--cream);font-size:21px;line-height:25px}
.tally{position:absolute;top:70px;left:55px;width:439px;list-style:none;font-family:"Rubik",sans-serif;font-size:13.2px;line-height:15.9px;color:var(--white)}
.tally li{text-align:justify;text-align-last:justify;white-space:nowrap}
.tally b{font-weight:700}
.cheat{position:absolute;top:297px;left:0;width:100%;text-align:center;color:var(--cream);font-size:27px}
.verdict-frame{position:absolute;left:20px;top:588px;width:489px;height:58px;border:3px solid var(--ink);border-top:none}
.verdict-frame__top{position:absolute;top:0;height:3px;background:var(--ink);width:124px}
.verdict-frame__top--l{left:0}.verdict-frame__top--r{right:0}
.verdict-line{position:absolute;left:0;width:100%;text-align:center;color:var(--ink)}
.verdict-line--1{top:-17px;font-size:28px}
.verdict-line--2{top:14px;font-size:26px}
</style>
</head>
<body>
<main class="canvas">
  <section class="card card--front" aria-label="Mailer front">
    <h1 class="title heading">
      <span class="title__name">Esteban</span>
      <span class="title__grade">9TH<br>GRADE</span>
      <span class="title__name">Quintero!</span>
    </h1>
    <div class="front__band">
      <div class="quote-frame">
        <span class="quote-frame__top quote-frame__top--l"></span>
        <span class="quote-frame__top quote-frame__top--r"></span>
      </div>
      <p class="quote-ask heading">WHAT'S THAT FAMOUS SAYING?</p>
      <p class="quote heading">SHOW ME WHO YOUR FRIENDS ARE AND<br>I'LL TELL YOU WHO YOU REALLY ARE!</p>
      <div class="friends-photo" role="img" aria-label="Photo of Esteban Quintero and Arturo Benavides smiling side by side in campaign shirts"></div>
    </div>
    <p class="front__note heading">ARTURO BENAVIDES IS CHARGED WITH VOTER FRAUD BY CHANGING VOTER<br>ADDRESSES FROM ACROSS THE RGV SO THEY COULD VOTE IN EDINBURG</p>
  </section>

  <section class="card card--back" aria-label="Mailer back">
    <div class="question-panel">
      <h2 class="question heading">DID ESTEBAN (9TH GRADE)<br>QUINTERO COMMIT VOTER<br>FRAUD WHEN HE RAN<br>FOR OFFICE IN 2016?</h2>
      <div class="roster-photo" role="img" aria-label="Blurred photo of a printed voter roster with addresses"></div>
    </div>
    <div class="back__band">
      <p class="list-intro heading">HERE IS A LIST OF PEOPLE FROM ALL OVER THE RGV THAT VOTED IN<br>EDINBURG IN THE 2016 RACE. HERE IS A BREAK DOWN:</p>
      <ul class="tally">
        <li><b>9 People</b> voted in Edinburg who were registered in <b>Donna.</b></li>
        <li><b>13 People</b> voted in Edinburg who were registered in <b>San Juan</b></li>
        <li><b>8 People</b> voted in Edinburg who were registered in <b>Pharr</b></li>
        <li><b>31 People</b> voted in Edinburg who were registered in <b>McAllen</b></li>
        <li><b>2 People</b> voted in Edinburg who were registered in <b>La Joya</b></li>
        <li><b>6 People</b> voted in Edinburg who were registered in <b>Edcouch</b></li>
        <li><b>2 People</b> voted in Edinburg who were registered in <b>Mercedes</b></li>
        <li><b>2 People</b> voted in Edinburg who were registered in <b>Monte Alto</b></li>
        <li><b>6 People</b> voted in Edinburg who were registered in <b>Weslaco</b></li>
        <li><b>1 Person</b> voted in Edinburg who were registered in <b>Penitas</b></li>
        <li><b>3 People</b> voted in Edinburg who were registered in <b>Alamo</b></li>
        <li><b>5 People</b> voted in Edinburg who were registered in <b>Elsa</b></li>
        <li><b>6 People</b> voted in Edinburg who were registered in <b>Mission</b></li>
        <li><b>1 Person</b> voted in Edinburg who were registered in <b>Alton</b></li>
      </ul>
      <p class="cheat heading">WILL ESTEBAN (9TH GRADE) QUINTERO CHEAT IN 2020?</p>
    </div>
    <div class="verdict-frame">
      <span class="verdict-frame__top verdict-frame__top--l"></span>
      <span class="verdict-frame__top verdict-frame__top--r"></span>
      <p class="verdict-line verdict-line--1 heading">ONLY TIME WILL TELL.</p>
      <p class="verdict-line verdict-line--2 heading">VOTE ESTEBAN (9TH GRADE) QUINTERO OUT OF OFFICE.</p>
    </div>
  </section>
</main>
</body>
</html>
```